Calder Wynd Company Profile

We have all the written content for our company profile and just need the background graphics and layout designed, this can be seen at our website www.calder-wynd.example or in the attached company profiles
We are happy with the content as far as wording and our logo are concerned, we are looking to revamp the background and layout.
The intention is for this to be printed as a brochure where the inside of the rear page has a pocket at the bottom so that our relevant affiliated companies brochures can be inserted into to complete the package depending on who we are presenting it to.

Target Market(s)

Oil & Gas, Power Generation, Mining, Maritime, Marine, Automation, Engineering

Industry/Entity Type

Engineering Consulting

Colors

Designer to choose colors to be used in the design.

Requirements
Must have
• Existing provided content
Nice to have
• engineering background and images that pop
Should not have
• our target market is Oil & Gas, Power Generation, Mining, Maritime, Marine, Automation, Engineering so it should not have content that does not relate to these industries

```html
<!DOCTYPE html>
<html lang="en">
<head>
<meta charset="utf-8">
<title>Calder Wynd – Our Mission</title>
<link rel="stylesheet" href="https://fonts.googleapis.com/css2?family=Noto+Sans:wght@400;700&family=Saira+Semi+Condensed:wght@700&display=swap">
<style>
  :root {
    --ink: #1c1c1c;
    --paper: #ffffff;
    --orange: #f5a623;
    --caption: #f7b43a;
    --panel: #5e4a33;
    --footer: #5a5a5a;
    --footer-light: #7a7a7a;
    --logo-ink: #3f3f3f;
  }
  * { margin: 0; padding: 0; box-sizing: border-box; }
  html, body { width: 848px; height: 1200px; overflow: hidden; background: var(--paper); }
  .page {
    position: relative; width: 848px; height: 1200px; overflow: hidden;
    background: var(--paper); color: var(--ink);
    font-family: "Noto Sans", Verdana, sans-serif;
  }
  .text-column {
    position: absolute; left: 17px; top: 14px; width: 538px;
    hyphens: auto; -webkit-hyphens: auto;
  }
  .section-title { font-size: 25px; font-weight: 700; line-height: 30px; }
  .sub-title { font-size: 19px; font-weight: 700; line-height: 26px; margin-top: 20px; }
  .body-copy { font-size: 15.6px; line-height: 23px; letter-spacing: 0.35px; margin-top: 16px; }
  .section-title + .sub-title { margin-top: 20px; }
  .values-title { margin-top: 40px; }
  .values-title + .sub-title { margin-top: 14px; }
  .gap-large { margin-top: 30px; }

  .case-card {
    position: absolute; left: 574px; width: 274px; min-height: 258px;
    background: var(--panel); border: 7px solid var(--orange); border-right: none;
    padding: 12px 14px 10px 10px;
    display: flex; flex-direction: column;
  }
  .case-photo { width: 244px; height: 172px; border: 2px solid #e9e2d4; flex: none; }
  .case-caption {
    margin-top: 8px; color: var(--caption);
    font-size: 10.8px; line-height: 13.5px;
    hyphens: auto; -webkit-hyphens: auto;
  }
  .photo-penstock { background: radial-gradient(circle at 50% 45%, #c9c0b0 0%, #6e6256 40%, #2b241f 80%); }
  .photo-mine { background: linear-gradient(180deg, #8f8a7e 0%, #b6a27a 55%, #cfc8b8 100%); }
  .photo-plant { background: linear-gradient(180deg, #c8cdcb 0%, #9aa39c 50%, #4e5c49 100%); }

  .footer { position: absolute; left: 0; top: 1124px; width: 848px; height: 76px; }
  .footer-band { position: absolute; inset: 0; }
  .footer-contact {
    position: absolute; left: 17px; top: 10px;
    color: var(--orange); font-size: 10px; line-height: 14px;
    font-variant: small-caps; letter-spacing: 1.2px;
  }
  .brand-name {
    position: absolute; left: 640px; top: 12px;
    font-family: "Saira Semi Condensed", "Noto Sans", sans-serif; font-weight: 700;
    color: var(--logo-ink); font-size: 27px; line-height: 25px; letter-spacing: 1px;
  }
</style>
</head>
<body>
<main class="page">
  <section class="text-column">
    <h1 class="section-title">Our Mission</h1>
    <h2 class="sub-title">Purpose:</h2>
    <p class="body-copy">To provide qualified and motivated technical manpower and consultancy services to our clients worldwide.</p>
    <h2 class="sub-title">Commitment:</h2>
    <p class="body-copy">We strive to exceed the needs and expectations of our clients through exemplary professional and technical services with continuous quality improvement.</p>
    <h2 class="sub-title">Objective:</h2>
    <p class="body-copy">To continue building and maintaining our engineering team with the expertise for executing every project with success and total client satisfaction.</p>
    <h2 class="sub-title">Vision:</h2>
    <p class="body-copy">To become the ‘Industry’ world leader in our sector through customer satisfaction.</p>

    <h1 class="section-title values-title">Our Corporate Values</h1>
    <h2 class="sub-title">Ethical behaviour and integrity:</h2>
    <p class="body-copy">Our foundation is our integrity, and all stakeholders are responsible for abiding by and upholding our Code of Business Conduct and Ethics. We are open and encourage all stakeholders to raise issues and discuss differences of opinion. We are honest and trustworthy in dealing with customers, suppliers, contractors, representatives, co-workers, and shareholders and communities we affect.</p>
    <h2 class="sub-title gap-large">Commitment to customers:</h2>
    <p class="body-copy">Our priority is to please our customers by providing the highest quality of services consistent with their requirements and specifications. We treat our customers fairly in all aspects of our business transactions, including remedies for any dissatisfaction. We strive to build strong and long term relationships with our customers, and support their success by creating exceptional value through confidentiality, collaboration, continuous improvement, change, and innovation to meet their ever-changing needs.</p>
  </section>

  <figure class="case-card" style="top:133px">
    <div class="case-photo photo-penstock" role="img" aria-label="Workers inside a hydro power station penstock during repair"></div>
    <figcaption class="case-caption">Hydro power station penstock repair, Philippines</figcaption>
  </figure>
  <figure class="case-card" style="top:410px">
    <div class="case-photo photo-mine" role="img" aria-label="Large excavator and crew at an open-pit mine site"></div>
    <figcaption class="case-caption">Heavy equipment maintenance management, support and repair 36 x units of various heavy equipment at a major mine site in the Philippines. Philippines.</figcaption>
  </figure>
  <figure class="case-card" style="top:705px">
    <div class="case-photo photo-plant" role="img" aria-label="Hydro electric power plant building in misty forested hills"></div>
    <figcaption class="case-caption">Excitation system commissioning for 4 x units 170 MW turbines at a hydro electric power plant in Portugal.</figcaption>
  </figure>

  <footer class="footer">
    <svg class="footer-band" width="848" height="76" viewBox="0 0 848 76" aria-hidden="true">
      <polygon points="0,0 560,0 600,76 0,76" fill="var(--footer)"/>
      <polygon points="560,0 848,0 848,76 600,76" fill="var(--footer-light)" opacity="0.35"/>
    </svg>
    <div class="footer-contact">
      Web: www.calder-wynd.example<br>
      Email: consultants@calder-wynd.example<br>
      Tel: +852-5550-0142<br>
      Address: Unit C-2, 16th Floor, Harbour Point 12 Meridian Road, Hong Kong
    </div>
    <div class="brand-name">CALDER<br>WYND</div>
  </footer>
</main>
</body>
</html>
```